Brackenridge Strength Studio Chronic Pain Flyer

Double sided DL flyer required to promote a strength training studio to sufferers of chronic pain. Flyer will be displayed in osteopathy, chiropractic and massage clinics. Flyer should be clean, professional and appeal to an older (40+) demographic.

Target Market(s)

Chronic pain sufferers. Age 40+

Industry/Entity Type

Health And Wellness

Colors

Designer to choose colors to be used in the design.

Requirements
Must have
• See attached files for text copy and logo. Image(s) of people strength training with a coach or personal trainer, as well as images depicting pain in common parts of the body (such as those pictured in the supplied mock up)
• website address: brackenridgestrengthstudio.example.com.au
• phone number : 0452 918 304
• Street address: 4/63 Juniper Hollow Rd, Brackenridge
Nice to have
• Images such as in the attached files.

```html
<!DOCTYPE html>
<html lang="en">
<head>
<meta charset="utf-8">
<title>Brackenridge Strength Studio – Chronic Pain Flyer</title>
<link href="https://fonts.googleapis.com/css2?family=Open+Sans:wght@300;400;600;700&display=swap" rel="stylesheet">
<style>
  :root {
    --backdrop: #7d7d7d;
    --paper: #ffffff;
    --ink: #3f3f3f;
    --ink-soft: #555555;
    --red-deep: #9b1c24;
    --red-bright: #ef3a35;
    --frame: #6a6a6a;
  }
  * { margin: 0; padding: 0; box-sizing: border-box; }
  html, body { width: 1200px; height: 1200px; overflow: hidden; }
  body {
    background: radial-gradient(circle at 50% 40%, #9a9a9a, var(--backdrop) 75%);
    font-family: "Open Sans", Arial, sans-serif;
    color: var(--ink);
    position: relative;
  }
  .flyer {
    position: absolute;
    top: 116px;
    width: 496px;
    height: 988px;
    background: var(--paper);
    overflow: hidden;
    box-shadow: 3px 4px 6px rgba(0,0,0,0.35);
  }
  .flyer--front { left: 86px; background: linear-gradient(180deg, #d9d9da 0%, #ececec 45%, #e6e6e6 70%, #ffffff 70%); }
  .flyer--back { left: 612px; }
  .photo { position: absolute; }
  .photo--front {
    left: 40px; top: 380px; width: 416px; height: 360px;
    background: radial-gradient(ellipse at 50% 45%, #f3f3f3 0%, #e2dfdd 45%, #e6e6e6 75%, rgba(230,230,230,0) 100%);
  }
  .photo--back {
    left: 0; top: 420px; width: 496px; height: 400px;
    background: linear-gradient(180deg, #ffffff 0%, #f1ece8 25%, #e8d6cb 55%, #d9c3b6 80%, #e4d7cf 100%);
  }
  .curves { position: absolute; left: 0; top: 0; width: 496px; height: 988px; }
  .brand {
    position: absolute; top: 168px; left: 0; width: 100%;
    text-align: center; font-weight: 700; font-size: 25px; line-height: 1.15;
    color: var(--ink-soft); letter-spacing: 1px; text-transform: uppercase;
  }
  .headline { position: absolute; left: 0; width: 100%; text-align: center; }
  .headline__lead { font-weight: 400; color: var(--ink); letter-spacing: 0.5px; display: block; line-height: 1; }
  .headline__main { font-weight: 700; color: var(--red-deep); display: block; line-height: 1; }
  .flyer--front .headline { top: 276px; }
  .flyer--front .headline__lead { font-size: 43px; }
  .flyer--front .headline__main { font-size: 71px; margin-top: 2px; }
  .flyer--back .headline { top: 36px; }
  .flyer--back .headline__lead { font-size: 44px; }
  .flyer--back .headline__main { font-size: 74px; margin-top: 0; }
  .tagline {
    position: absolute; top: 154px; left: 0; width: 100%; text-align: center;
    font-size: 22px; color: var(--ink); letter-spacing: 0.3px;
  }
  .body-copy {
    position: absolute; left: 28px; width: 440px;
    font-size: 15.5px; line-height: 23px; color: var(--ink-soft); text-align: justify;
  }
  .body-copy--intro { top: 205px; text-align: left; }
  .body-copy--offer { top: 330px; }
  .call-box {
    position: absolute; left: 46px; width: 404px; height: 88px;
    border: 1.5px solid var(--frame);
  }
  .flyer--front .call-box { top: 778px; }
  .flyer--back .call-box { top: 782px; }
  .call-box__label {
    position: absolute; top: -24px; left: 50%; transform: translateX(-50%);
    background: var(--paper); padding: 0 6px; white-space: nowrap;
    font-size: 37px; font-weight: 400; color: var(--ink-soft); line-height: 1.2;
  }
  .call-box__phone {
    position: absolute; top: 25px; left: 0; width: 100%; text-align: center;
    font-size: 52px; font-weight: 700; color: var(--red-bright); line-height: 1.1; letter-spacing: -0.5px;
  }
  .call-box::after {
    content: ""; position: absolute; left: 10%; right: 10%; bottom: -14px; height: 10px;
    background: radial-gradient(ellipse at center, rgba(0,0,0,0.18), rgba(0,0,0,0) 70%);
  }
  .contact { position: absolute; left: 0; width: 100%; text-align: center; }
  .flyer--front .contact { top: 894px; }
  .flyer--back .contact { top: 898px; }
  .contact__web { display: block; font-size: 14.5px; font-weight: 600; letter-spacing: 0.6px; color: var(--ink-soft); text-transform: uppercase; }
  .contact__address { display: block; margin-top: 6px; font-size: 24px; font-weight: 600; color: var(--ink-soft); }
</style>
</head>
<body>

<section class="flyer flyer--front">
  <div class="photo photo--front" role="img" aria-label="Photo of a woman seen from behind, holding her neck and lower back, with red glow marking the pain areas"></div>
  <svg class="curves" viewBox="0 0 496 988" aria-hidden="true">
    <path d="M0,596 C140,700 320,725 496,680 L496,988 L0,988 Z" fill="var(--red-deep)"/>
    <path d="M250,718 C380,702 450,662 496,600 L496,640 C440,704 360,726 250,718 Z" fill="var(--red-bright)"/>
    <path d="M0,640 C150,730 340,742 496,640 L496,988 L0,988 Z" fill="var(--paper)"/>
  </svg>
  <div class="brand">Brackenridge<br>Strength Studio</div>
  <h1 class="headline">
    <span class="headline__lead">HEALTH THROUGH</span>
    <span class="headline__main">STRENGTH</span>
  </h1>
  <div class="call-box">
    <span class="call-box__label">CALL US TODAY</span>
    <span class="call-box__phone">0452 918 304</span>
  </div>
  <p class="contact">
    <span class="contact__web">brackenridgestrengthstudio.example.com.au</span>
    <span class="contact__address">4/63 Juniper Hollow Rd, Brackenridge</span>
  </p>
</section>

<section class="flyer flyer--back">
  <div class="photo photo--back" role="img" aria-label="Photo of a person holding a sore knee with both hands, red glow marking the pain"></div>
  <svg class="curves" viewBox="0 0 496 988" aria-hidden="true">
    <path d="M0,788 C110,700 260,668 420,676 C460,678 496,700 496,760 L496,988 L0,988 Z" fill="var(--red-deep)"/>
    <path d="M180,694 C340,664 460,690 496,745 L496,900 C400,764 300,722 180,694 Z" fill="var(--red-bright)"/>
    <path d="M0,840 C140,730 330,705 496,805 L496,988 L0,988 Z" fill="var(--paper)"/>
  </svg>
  <h2 class="headline">
    <span class="headline__lead">HEALTH THROUGH</span>
    <span class="headline__main">STRENGTH</span>
  </h2>
  <p class="tagline">YOU DON’T HAVE TO LIVE IN PAIN.</p>
  <p class="body-copy body-copy--intro">Strength training has been shown to improve many chronic pain conditions and is now being routinely recommended by medical and health professionals.</p>
  <p class="body-copy body-copy--offer">Our private studio provides high quality strength training by expert strength coaches. We’ve helped countless people improve or eliminate chronic pain, contact us today and find out how we can help you.</p>
  <div class="call-box">
    <span class="call-box__label">CALL US TODAY</span>
    <span class="call-box__phone">0452 918 304</span>
  </div>
  <p class="contact">
    <span class="contact__web">brackenridgestrengthstudio.example.com.au</span>
    <span class="contact__address">4/63 Juniper Hollow Rd, Brackenridge</span>
  </p>
</section>

</body>
</html>
```